The Pebble Finch Leaflet. A5 2-sided Flyer for a UK Lawn Treatment Company

I need an A5 two-side leaflet / flyer designed for my Lawn Treatment company. The leaflet will be for door-drops so quick impact needed. Full colour, both sides. I provide lawn treatments to customers in the Exeter area of Devon. I would like to design to be clear, fresh and reflect the joy a good lawn and garden can bring.

Target Market(s)

Home Owners. 30-80 Years. Familys

Font styles to use
Sans Serif

Colors
9bcb3c
f78f20
ec1f27
33a6d7

Requirements
Must have
• Good front page picture
• Logo
• Contact details on front.
• Call to Action
• More details in Text file included in design.
Nice to have
• Clipart of a family / lady enjoying a lawn.

```html
<!DOCTYPE html>
<html lang="en">
<head>
<meta charset="utf-8">
<title>The Pebble Finch – A5 Leaflet</title>
<link href="https://fonts.googleapis.com/css2?family=Lato:ital,wght@0,400;0,700;1,400&family=Roboto+Slab:wght@300;400&display=swap" rel="stylesheet">
<style>
  :root {
    --backdrop: #e4e4e2;
    --paper: #f2f2f2;
    --green-deep: #1b7a3c;
    --green-text: #237b3e;
    --lime: #8cc63f;
    --orange: #f39229;
    --grey-text: #4a4a4a;
  }
  * { box-sizing: border-box; margin: 0; padding: 0; }
  html, body { width: 1200px; height: 931px; overflow: hidden; }
  body { background: var(--backdrop); font-family: "Lato", sans-serif; position: relative; }

  .flyer {
    position: absolute; top: 101px; width: 514px; height: 729px;
    background: var(--paper); overflow: hidden;
    box-shadow: 0 2px 6px rgba(0,0,0,.18);
  }
  .flyer--front { left: 66px; }
  .flyer--back { left: 620px; }
  .flyer__header { position: absolute; left: 0; top: 0; width: 514px; height: 330px; }

  .brand {
    position: absolute; left: 0; right: 0; top: 350px; height: 44px;
    display: flex; align-items: center; justify-content: center; gap: 12px;
  }
  .brand__dot { width: 16px; height: 16px; border-radius: 50%; background: var(--lime); }
  .brand__name {
    font-family: "Roboto Slab", serif; font-weight: 400; font-size: 30px;
    color: var(--green-text); letter-spacing: .5px; text-transform: uppercase; white-space: nowrap;
  }

  .headline {
    position: absolute; left: 0; right: 0; text-align: center;
    font-family: "Roboto Slab", serif; font-weight: 400; color: var(--green-text);
  }
  .flyer--front .headline { top: 424px; font-size: 24px; line-height: 30px; text-transform: uppercase; }
  .flyer--back .headline { top: 418px; font-size: 24px; line-height: 30px; }

  .outline-box {
    position: absolute; left: 147px; width: 219px; height: 29px;
    border: 1.5px solid var(--orange); background: #fff;
    display: flex; align-items: center; justify-content: center;
    font-size: 15px; color: var(--grey-text);
  }
  .flyer--front .outline-box { top: 495px; }
  .flyer--back .outline-box { top: 492px; color: var(--green-text); font-size: 14px; }

  .line { position: absolute; left: 0; right: 0; text-align: center; font-size: 15.5px; color: var(--grey-text); }

  .testimonial {
    position: absolute; left: 32px; top: 595px; width: 448px; height: 62px;
    border: 1.5px solid var(--lime); border-radius: 4px; background: #fff;
    padding: 14px 14px 0; text-align: center;
    font-style: italic; font-size: 8.6px; line-height: 12.5px; color: #6a6a6a;
  }
  .testimonial__mark {
    position: absolute; top: -12px; left: 50%; transform: translateX(-50%);
    background: var(--paper); padding: 0 4px;
    font-family: "Roboto Slab", serif; font-size: 30px; line-height: 22px; color: var(--lime); font-style: normal;
  }

  .intro {
    position: absolute; left: 14px; right: 14px; top: 454px; text-align: center;
    font-size: 9.8px; line-height: 13px; color: var(--grey-text);
  }
  .services-title {
    position: absolute; left: 16px; top: 538px;
    font-family: "Roboto Slab", serif; font-weight: 400; font-size: 17px; color: var(--green-text);
  }
  .services-text {
    position: absolute; left: 16px; right: 20px; top: 561px;
    font-size: 11px; line-height: 13.5px; color: var(--grey-text);
  }
  .services-list {
    position: absolute; left: 18px; top: 593px; width: 480px;
    list-style: none; display: grid; grid-template-columns: 125px 125px 200px;
    grid-auto-flow: column; grid-template-rows: repeat(3, 17.5px);
    font-size: 11.5px; color: var(--grey-text);
  }
  .services-list li { display: flex; align-items: center; gap: 8px; white-space: nowrap; }
  .services-list svg { width: 9px; height: 9px; flex: none; }

  .web-pill {
    position: absolute; left: 107px; top: 667px; width: 300px; height: 31px;
    background: var(--green-deep); border-radius: 8px; z-index: 2;
    display: flex; align-items: center; justify-content: center;
    font-family: "Roboto Slab", serif; font-size: 17px; color: #fff; letter-spacing: .3px;
    box-shadow: 0 2px 3px rgba(0,0,0,.2);
  }
  .footer-band {
    position: absolute; left: 0; right: 0; bottom: 0; height: 43px;
    background: var(--lime); color: #fff; font-size: 14px;
    display: flex; align-items: flex-end; justify-content: center; padding-bottom: 9px;
    white-space: nowrap;
  }
  .footer-band strong { font-weight: 700; }
</style>
</head>
<body>

<section class="flyer flyer--front">
  <svg class="flyer__header" viewBox="0 0 514 330">
    <defs>
      <linearGradient id="front-photo" x1="0" y1="0" x2="0" y2="1">
        <stop offset="0" stop-color="#9fb58a"/>
        <stop offset=".35" stop-color="#5f8f3a"/>
        <stop offset=".6" stop-color="#7fbf3f"/>
        <stop offset="1" stop-color="#6fae36"/>
      </linearGradient>
      <linearGradient id="circle-fill" x1="0" y1="0" x2="0" y2="1">
        <stop offset="0" stop-color="#3f7f2a"/>
        <stop offset="1" stop-color="#7fbf3f"/>
      </linearGradient>
    </defs>
    <rect role="img" aria-label="Photo of a house front garden with a green lawn and colourful flower beds" x="0" y="0" width="514" height="320" fill="url(#front-photo)"/>
    <path d="M0 282 C150 270 360 300 514 208 L514 232 C360 318 150 290 0 312 Z" fill="var(--lime)"/>
    <path d="M0 296 C60 284 120 280 175 282 L175 290 C120 290 60 296 0 318 Z" fill="var(--orange)"/>
    <path d="M0 312 C150 290 360 318 514 232 L514 330 L0 330 Z" fill="var(--paper)"/>
    <circle cx="98" cy="263" r="60" fill="#fff" stroke="var(--orange)" stroke-width="1.5"/>
    <circle role="img" aria-label="Photo of a striped lawn beside tall trees" cx="98" cy="263" r="53" fill="url(#circle-fill)"/>
    <circle cx="257" cy="263" r="60" fill="#fff" stroke="var(--orange)" stroke-width="1.5"/>
    <circle role="img" aria-label="Photo of a close-up of a freshly cut lawn" cx="257" cy="263" r="53" fill="url(#circle-fill)"/>
    <circle cx="426" cy="263" r="60" fill="#fff" stroke="var(--orange)" stroke-width="1.5"/>
    <circle role="img" aria-label="Photo of a lawn edged with clipped hedges" cx="426" cy="263" r="53" fill="url(#circle-fill)"/>
  </svg>

  <div class="brand"><span class="brand__dot"></span><span class="brand__name">The Pebble Finch</span></div>

  <h1 class="headline">Treatments &amp; advice to keep your<br>lawn looking nice.</h1>

  <div class="outline-box">Brand new to the area!</div>
  <p class="line" style="top:527px">8 Years experience maintaining the finest lawns of Cheshire</p>
  <p class="line" style="top:558px">Complete Satisfaction Guarantee!</p>

  <blockquote class="testimonial">
    <span class="testimonial__mark">&ldquo;</span>
    Thank you for the lawn service you have provided over the years. It is reassuring to have you come round
    as I know you carried out the service as promised unlike other lawn service companies I have dealt with.<br>- Martin
  </blockquote>

  <div class="web-pill">www.thepebblefinch.co.uk</div>
  <div class="footer-band"><span>Call today on <strong>01632 960418</strong> or text <strong>07700 900512</strong> to book your lawn survey</span></div>
</section>

<section class="flyer flyer--back">
  <svg class="flyer__header" viewBox="0 0 514 330">
    <defs>
      <linearGradient id="back-photo" x1="0" y1="0" x2="0" y2="1">
        <stop offset="0" stop-color="#4f7f2f"/>
        <stop offset=".45" stop-color="#6aa83a"/>
        <stop offset="1" stop-color="#86c444"/>
      </linearGradient>
      <linearGradient id="before-fill" x1="0" y1="0" x2="0" y2="1">
        <stop offset="0" stop-color="#4d6a2e"/>
        <stop offset="1" stop-color="#a2a55a"/>
      </linearGradient>
      <linearGradient id="after-fill" x1="0" y1="0" x2="0" y2="1">
        <stop offset="0" stop-color="#3f7f2a"/>
        <stop offset="1" stop-color="#5fae36"/>
      </linearGradient>
    </defs>
    <rect role="img" aria-label="Photo of a striped lawn with a gravel path leading to a white garden arbour" x="0" y="0" width="514" height="300" fill="url(#back-photo)"/>
    <path d="M0 270 C160 250 360 250 514 222 L514 238 C360 270 160 272 0 292 Z" fill="var(--lime)"/>
    <path d="M0 282 C50 276 110 266 170 262 L170 268 C110 274 50 286 0 302 Z" fill="var(--orange)"/>
    <path d="M0 292 C160 272 360 270 514 238 L514 330 L0 330 Z" fill="var(--paper)"/>
    <circle cx="321" cy="256" r="62" fill="#fff" stroke="var(--orange)" stroke-width="1.5"/>
    <circle role="img" aria-label="Photo of a patchy lawn before treatment" cx="321" cy="256" r="55" fill="url(#before-fill)"/>
    <text x="321" y="263" text-anchor="middle" font-family="Roboto Slab, serif" font-size="17" fill="#fff">BEFORE</text>
    <circle cx="432" cy="243" r="64" fill="#fff" stroke="var(--orange)" stroke-width="1.5"/>
    <circle role="img" aria-label="Photo of a lush green lawn after treatment" cx="432" cy="243" r="57" fill="url(#after-fill)"/>
    <text x="432" y="250" text-anchor="middle" font-family="Roboto Slab, serif" font-size="17" fill="#fff">AFTER</text>
  </svg>

  <div class="brand"><span class="brand__dot"></span><span class="brand__name">The Pebble Finch</span></div>

  <h2 class="headline">For a beautiful weed-free lawn</h2>
  <p class="intro">Call The Pebble Finch today and start your journey to a wonderful, lush, green lawn you and your family can enjoy. Arrange a no-obligation lawn survey and quotation at a time to suit you.</p>

  <div class="outline-box">Call 01632 960418 now.</div>

  <h3 class="services-title">Industry-leading lawn care</h3>
  <p class="services-text">I have 8 years of experience in the leading edge of domestic lawn care. I have a comprehensive range of treatments including:</p>

  <ul class="services-list">
    <li><svg viewBox="0 0 10 10"><circle cx="5" cy="5" r="5" fill="var(--lime)"/><path d="M4 3l2 2-2 2" stroke="#fff" stroke-width="1.3" fill="none"/></svg>Scarification</li>
    <li><svg viewBox="0 0 10 10"><circle cx="5" cy="5" r="5" fill="var(--lime)"/><path d="M4 3l2 2-2 2" stroke="#fff" stroke-width="1.3" fill="none"/></svg>Aeration</li>
    <li><svg viewBox="0 0 10 10"><circle cx="5" cy="5" r="5" fill="var(--lime)"/><path d="M4 3l2 2-2 2" stroke="#fff" stroke-width="1.3" fill="none"/></svg>Moss Control</li>
    <li><svg viewBox="0 0 10 10"><circle cx="5" cy="5" r="5" fill="var(--lime)"/><path d="M4 3l2 2-2 2" stroke="#fff" stroke-width="1.3" fill="none"/></svg>Overseeding</li>
    <li><svg viewBox="0 0 10 10"><circle cx="5" cy="5" r="5" fill="var(--lime)"/><path d="M4 3l2 2-2 2" stroke="#fff" stroke-width="1.3" fill="none"/></svg>Top Dressing</li>
    <li><svg viewBox="0 0 10 10"><circle cx="5" cy="5" r="5" fill="var(--lime)"/><path d="M4 3l2 2-2 2" stroke="#fff" stroke-width="1.3" fill="none"/></svg>Lawn Repairs</li>
    <li><svg viewBox="0 0 10 10"><circle cx="5" cy="5" r="5" fill="var(--lime)"/><path d="M4 3l2 2-2 2" stroke="#fff" stroke-width="1.3" fill="none"/></svg>Fertilisation &amp; Weed Control</li>
    <li><svg viewBox="0 0 10 10"><circle cx="5" cy="5" r="5" fill="var(--lime)"/><path d="M4 3l2 2-2 2" stroke="#fff" stroke-width="1.3" fill="none"/></svg>Pest and Disease Management</li>
    <li><svg viewBox="0 0 10 10"><circle cx="5" cy="5" r="5" fill="var(--lime)"/><path d="M4 3l2 2-2 2" stroke="#fff" stroke-width="1.3" fill="none"/></svg>Special Event Preparation</li>
  </ul>

  <div class="web-pill">www.thepebblefinch.co.uk</div>
  <div class="footer-band"><span>Save time and money and leave your lawn to an expert. Call <strong>01632 960418</strong> Today.</span></div>
</section>

</body>
</html>
```